Letterhead Design Project

We are looking for a simple letterhead design that reflects our core purpose. We help our clients gain clarity and focus but we are there to help them execute. The letterhead design would mainly be utilised for engagement letters and contracts.

Target Market(s)

The customers of our business are large corporate organisations.

Requirements
Must have
• The letterhead must have the company logo
The font used must tie in to the font used in the company logo

Must have the following business details
Address: Level 10, 27 Brimley Lane, Melbourne, Australia, 3000
Phone: +61 3 502 847 193
Fax: +61 3 9412 5037
Website: www.vorndex.com.au
Twiiter: @vorndex

```html
<!DOCTYPE html>
<html lang="en">
<head>
<meta charset="utf-8">
<title>Vorndex Letterhead</title>
<link href="https://fonts.googleapis.com/css2?family=Arimo:wght@400&display=swap" rel="stylesheet">
<style>
  :root {
    --brand-blue: #0a4cf5;
    --arc-grey: #3f3f41;
    --paper: #ffffff;
    --backdrop: #e8e6e2;
    --ink: #111111;
  }
  * { margin: 0; padding: 0; box-sizing: border-box; }
  html, body {
    width: 927px;
    height: 1200px;
    overflow: hidden;
    background: var(--backdrop);
    font-family: "Arimo", Arial, sans-serif;
  }
  .letterhead {
    position: absolute;
    left: 35px;
    top: 58px;
    width: 853px;
    height: 1105px;
    background: var(--paper);
  }
  .header-arc {
    position: absolute;
    left: 0;
    top: 0;
    display: block;
  }
  .brand {
    position: absolute;
    top: 72px;
    left: 0;
    width: 853px;
    display: flex;
    justify-content: center;
    align-items: center;
    gap: 12px;
    padding-left: 40px;
  }
  .brand-name {
    font-size: 60px;
    font-weight: 400;
    color: var(--brand-blue);
    letter-spacing: 1px;
    line-height: 1;
  }
  .brand-dot {
    width: 56px;
    height: 56px;
    border: 3px solid var(--brand-blue);
    border-radius: 50%;
  }
  .contact {
    position: absolute;
    font-size: 14px;
    line-height: 17.5px;
    color: var(--ink);
  }
  .contact-left {
    left: 0;
    top: 1017px;
    padding-left: 17px;
    border-left: 7px solid var(--brand-blue);
    border-radius: 2px;
  }
  .contact-left li {
    list-style: none;
    display: flex;
    align-items: center;
    gap: 6px;
  }
  .contact-left svg { width: 12px; height: 12px; flex: none; }
  .contact-right {
    right: 0;
    top: 1024px;
    padding-right: 17px;
    border-right: 6px solid var(--brand-blue);
    text-align: right;
    font-style: normal;
  }
</style>
</head>
<body>
  <main class="letterhead">
    <svg class="header-arc" width="853" height="150" viewBox="0 0 853 150" aria-hidden="true">
      <path d="M0 0 H853 V117 Q426.5 -70 0 117 Z" fill="var(--brand-blue)"/>
      <path d="M0 122 Q426.5 -68 853 122 V145 Q426.5 -77 0 145 Z" fill="var(--arc-grey)"/>
    </svg>

    <header class="brand">
      <span class="brand-name">Vorndex</span>
      <span class="brand-dot" aria-hidden="true"></span>
    </header>

    <ul class="contact contact-left">
      <li>
        <svg viewBox="0 0 12 12" aria-hidden="true"><path d="M2.5 1 L4.5 3.5 L3.5 5 Q5 7.5 7 8.5 L8.5 7.5 L11 9.5 L9.5 11 Q4 10 1 3 Z" fill="none" stroke="#222" stroke-width="1"/></svg>
        +61 3 502 847 193
      </li>
      <li>
        <svg viewBox="0 0 12 12" aria-hidden="true"><path d="M1 4 Q6 0 11 4 L10 5.5 L8 4.5 L4 4.5 L2 5.5 Z" fill="#222"/><rect x="3" y="6" width="6" height="5" rx="1" fill="#222"/></svg>
        +61 3 9412 5037
      </li>
      <li>
        <svg viewBox="0 0 12 12" aria-hidden="true"><circle cx="6" cy="6" r="5" fill="none" stroke="#222"/><ellipse cx="6" cy="6" rx="2.2" ry="5" fill="none" stroke="#222"/><path d="M1 6 H11 M2 3.5 H10 M2 8.5 H10" stroke="#222" stroke-width="0.8"/></svg>
        www.vorndex.com.au
      </li>
      <li>
        <svg viewBox="0 0 12 12" aria-hidden="true"><rect x="0.5" y="0.5" width="11" height="11" rx="2" fill="#5fc7ea"/></svg>
        @vorndex
      </li>
    </ul>

    <address class="contact contact-right">
      Level 10, 27 Brimley Lane<br>
      Melbourne<br>
      Australia, 3000
    </address>
  </main>
</body>
</html>
```